KV Group

We need a new website for our company and since we had a very good work done for our logo in this site, we're back for the entire job.

Our company name is Marlowe Capital Group. We're adding files of examples of what we have done today. In my opinion we need a more attention lock in the site but yet financial simple work.

Our files (attached) will let you know what we have so far. We need a complete change but the colours should be the same, however you can change them not running away to far from the original, and of course matching with the logo.

We need examples for 3 kind of layouts.

- A HOME welcome layout
- An internal Layout with sidebar
- And internal Layout wide

We can buy image licenses if needed for assets.
Actually there are 5 slide images placed on the Welcome HOME, we need those there, but you can improve with better images to match the new website!!!

Target Market(s)

Clients looking for financial advisers, tax and funds specialist, currency advisers

Industry/Entity Type

Financial

Requirements
Must have
• all the fonts must be in accordance with the financial market sites........the welcome home page must be precise, neat and information accurate........the menu should be elegant........main focus on the Home page, should be also the PRIVATE ACCESS box log in.......

```html
<!DOCTYPE html>
<html lang="en">
<head>
<meta charset="utf-8">
<title>Marlowe Capital Group</title>
<link href="https://fonts.googleapis.com/css2?family=Arimo:wght@400;700&family=Lato:wght@400;700&family=Michroma&family=Ubuntu:wght@500;700&display=swap" rel="stylesheet">
<style>
:root{
  --orange:#ee6f1c;
  --orange-dark:#d9590c;
  --ink:#1d1d1d;
  --text:#555;
  --page:#efefef;
  --footer:#474747;
  --footer-deep:#3a3a3a;
  --footer-text:#e6e6e6;
  --rule:#d6d6d6;
}
*{box-sizing:border-box;margin:0;padding:0}
html,body{width:878px;height:1200px;overflow:hidden}
body{position:relative;background:var(--page);font-family:'Arimo',Arial,sans-serif;color:var(--text)}
.abs{position:absolute}
.header{left:0;top:0;width:878px;height:106px;background:linear-gradient(#fff 0,#fff 60%,#f0f0f0 100%)}
.brand{left:100px;top:40px;display:flex;align-items:center;gap:8px;font-family:'Arimo',sans-serif;font-weight:700;font-size:15px;color:var(--ink);letter-spacing:.5px}
.brand-mark{width:14px;height:14px;background:var(--orange)}
.util{top:27px;display:flex;align-items:center;gap:6px;font-size:10px;color:#333}
.util svg{width:14px;height:13px}
.util-sep{left:694px;top:27px;width:1px;height:14px;background:#ccc}
.nav{left:97px;top:82px;width:684px;height:24px;background:linear-gradient(#eaeaea,#cfcfcf);display:flex;font-size:10.5px;color:#222}
.nav a{display:flex;align-items:center;justify-content:center;text-decoration:none;color:inherit;border-right:1px solid #b9b9b9;height:100%}
.nav a.active{background:var(--orange);color:#fff;font-weight:700}
.city{left:0;top:106px;width:878px;height:262px;background:linear-gradient(180deg,#5c7591 0%,#364658 55%,#8a6a45 100%)}
.hero-frame{left:96px;top:111px;width:686px;height:274px;background:#fff;border-radius:4px;box-shadow:0 6px 14px rgba(0,0,0,.25)}
.hero-img{left:102px;top:119px;width:672px;height:260px;border-radius:3px;background:linear-gradient(90deg,#eef1f4 0%,#d5dde6 30%,#5a7594 60%,#233a5b 100%)}
.hero-title{left:114px;top:138px;font-family:'Ubuntu',sans-serif;font-weight:700;font-size:27px;line-height:27px;color:#222;white-space:nowrap}
.hero-copy{left:115px;top:213px;width:215px;font-weight:700;font-size:12.6px;line-height:18.5px;color:#333}
.dot{top:362px;width:8px;height:8px;border-radius:50%;background:#888}
.dot.on{background:var(--orange)}
.sec-title{font-family:'Michroma',sans-serif;font-size:14px;letter-spacing:1px;font-variant:small-caps;white-space:nowrap}
.sec-title .o{color:var(--orange)}
.sec-title .d{color:var(--ink)}
.rule{height:1px;background:var(--rule)}
.body-copy{font-size:8.2px;line-height:14.6px;color:#555}
.btn{height:16px;background:linear-gradient(#f68a35,var(--orange-dark));color:#fff;font-weight:700;font-size:8px;display:flex;align-items:center;justify-content:center;border-radius:2px}
.field{left:574px;width:194px;height:24px;border:1px solid #c9c9c9;background:#fff;border-radius:2px;font-size:8.5px;color:#555;padding:7px 7px}
.card{top:586px;width:210px;height:186px;background:#fff;border:4px solid #e3e3e3;border-radius:6px;box-shadow:0 6px 6px -3px rgba(0,0,0,.35)}
.card h3{position:absolute;left:7px;top:7px;font-family:'Michroma',sans-serif;font-weight:400;font-size:10.5px;letter-spacing:.8px;font-variant:small-caps;color:var(--orange);white-space:nowrap}
.card .pic{position:absolute;left:6px;top:26px;width:189px;height:88px}
.card p{position:absolute;left:5px;top:124px;width:196px;font-family:'Lato',sans-serif;font-size:9.3px;line-height:12.5px;color:#555}
.card .more{position:absolute;right:10px;top:164px;font-family:'Lato',sans-serif;font-weight:700;font-size:8px;color:#444;text-decoration:underline}
.ticker{left:102px;top:805px;width:673px;height:24px;background:linear-gradient(#e8e8e8,#d2d2d2);border-radius:4px;box-shadow:0 5px 5px -3px rgba(0,0,0,.3);display:flex;align-items:center;justify-content:space-between;padding:0 13px;font-size:8px;font-weight:700;color:#333}
.ticker .v{color:var(--orange);margin-left:4px}
.ticker .up{color:var(--orange);margin-left:4px;font-size:7px}
.verified{left:0;top:850px;width:878px;text-align:center;font-family:'Michroma',sans-serif;font-size:10.5px;letter-spacing:1.6px;font-variant:small-caps;color:#222}
.badge{top:877px;height:26px;border-radius:13px;background:#d9d9d9}
.footer{left:0;top:925px;width:878px;height:193px;background:var(--footer)}
.footer-base{left:0;top:1118px;width:878px;height:82px;background:var(--footer-deep)}
.fcol{top:938px}
.fcol h4{font-family:'Michroma',sans-serif;font-weight:400;font-size:11px;letter-spacing:.8px;font-variant:small-caps;color:var(--orange);padding-bottom:6px;border-bottom:1px solid #5c5c5c;white-space:nowrap}
.fcol ul{list-style:none;margin-top:7px}
.fcol li{font-size:8.2px;color:var(--footer-text);height:19px;line-height:11px;padding-left:12px;position:relative;white-space:nowrap}
.fcol li::before{content:"›";position:absolute;left:0;top:0;color:#bbb;font-size:9px}
.fcol.tight li{height:16.5px}
.legal{left:106px;top:1132px;width:660px;font-size:7.7px;line-height:12.4px;color:#9c9c9c}
.copy{left:106px;top:1181px;font-size:7.7px;color:#9c9c9c}
</style>
</head>
<body>

<div class="abs header"></div>
<div class="abs brand"><span class="brand-mark"></span>Marlowe Capital Group</div>

<div class="abs util" style="left:615px">
  <svg viewBox="0 0 14 13"><rect x="1" y="2" width="10" height="10" fill="none" stroke="#ee6f1c" stroke-width="1.5"/><path d="M6 8 L13 1" stroke="#ee6f1c" stroke-width="1.8"/></svg>Apply Now
</div>
<div class="abs util-sep"></div>
<div class="abs util" style="left:708px">
  <svg viewBox="0 0 14 13"><rect x="1" y="2" width="12" height="9" fill="#ee6f1c"/><path d="M1 2 L7 7 L13 2" stroke="#fff" stroke-width="1.2" fill="none"/></svg>Contact Us
</div>

<nav class="abs nav">
  <a class="active" style="width:73px">Home</a>
  <a style="width:79px">About Us</a>
  <a style="width:90px">Investments</a>
  <a style="width:64px">Funds</a>
  <a style="width:82px">Brokerage</a>
  <a style="width:83px">Exchange</a>
  <a style="width:80px;border-right:none">Accounts</a>
</nav>

<div class="abs city" role="img" aria-label="City skyline at dusk"></div>
<div class="abs hero-frame"></div>
<div class="abs hero-img" role="img" aria-label="Business team reviewing documents at a desk"></div>
<div class="abs hero-title">Teamwork for<br>your Benefit</div>
<div class="abs hero-copy">Duis autem vel eum iriure dolor in hendrerit in vulputate velit esse molestie consequat, vel illum sit dolore eu feugiat nulla facilisis</div>
<div class="abs dot on" style="left:722px"></div>
<div class="abs dot" style="left:736px"></div>
<div class="abs dot" style="left:750px"></div>

<!-- Welcome -->
<div class="abs sec-title" style="left:104px;top:419px"><span class="o">Welcome to</span> <span class="d">Marlowe Capital</span></div>
<div class="abs rule" style="left:104px;top:442px;width:437px"></div>
<div class="abs body-copy" style="left:106px;top:449px;width:440px">Lorem ipsum dolor sit amet, consectetuer adipiscing elit, sed diam nonummy nibh euismod tincidunt ut laoreet sit dolore magna aliquam erat volutpat. Ut wisi enim ad minim veniam, quis nostrud exerci tation ullamcorper suscipit lobortis nisl ut aliquip ex ea commodo consequat. Duis autem vel eum iriure dolor in hendrerit in vulputate velit esse molestie consequat, vel illum dolore eu feugiat nulla facilisis at vero eros et accumsan et iusto odio dignissim qui blandit praesent luptatum zzril delenit augue duis dolore te feugait nulla facilisi. lenit augue duis dolore te feugait nul</div>
<div class="abs btn" style="left:487px;top:534px;width:57px">Read More</div>

<!-- Private access -->
<div class="abs sec-title" style="left:574px;top:419px"><span class="o">Private</span> <span class="d">Access</span></div>
<div class="abs rule" style="left:574px;top:442px;width:194px"></div>
<div class="abs field" style="top:450px">AC. Number</div>
<div class="abs field" style="top:482px">AC. Password</div>
<div class="abs" style="left:582px;top:515px;font-size:8.5px;color:#555">forgot acc number / password?</div>
<div class="abs btn" style="left:725px;top:534px;width:43px">Login</div>

<div class="abs rule" style="left:104px;top:565px;width:664px;background:linear-gradient(90deg,transparent,#d0d0d0,transparent)"></div>

<!-- Cards -->
<div class="abs card" style="left:103px">
  <h3>Management &amp; Strategy</h3>
  <div class="pic" role="img" aria-label="Hands reviewing financial charts with a pen" style="background:linear-gradient(#f4f4f4,#c9d3cf)"></div>
  <p>Lorem ipsum dolor sit amet, consectetuer delenit augue duis dolore te feugait nulla.Ut wisi enim ad minim veniam, quis</p>
  <span class="more">Read More »</span>
</div>
<div class="abs card" style="left:334px">
  <h3>Funds</h3>
  <div class="pic" role="img" aria-label="Blue stock market figures over a world map" style="background:linear-gradient(90deg,#2f6fb8,#6aaee6)"></div>
  <p>Lorem ipsum dolor sit amet, consectetuer delenit augue duis dolore te feugait nulla.Ut wisi enim ad minim veniam, quis</p>
  <span class="more">Read More »</span>
</div>
<div class="abs card" style="left:566px">
  <h3>Currency Exchange</h3>
  <div class="pic" role="img" aria-label="Green buy key and red sell key on a keyboard" style="background:linear-gradient(90deg,#2f9b3a 0%,#3bb14a 45%,#c81f1f 55%,#9e1414 100%)"></div>
  <p>Lorem ipsum dolor sit amet, consectetuer delenit augue duis dolore te feugait nulla.Ut wisi enim ad minim veniam, quis</p>
  <span class="more">Read More »</span>
</div>

<!-- Ticker -->
<div class="abs ticker">
  <span>GBP/UAH =<span class="v">12.65761</span><span class="up">▲</span></span>
  <span>GBP/UGX =<span class="v">4010.06174</span><span class="up">▼</span></span>
  <span>GBP/USD =<span class="v">1.55817</span><span class="up">▲</span></span>
  <span>GBP/UYU =<span class="v">34.36026</span><span class="up">▲</span></span>
  <span>GBP/VEF =<span class="v">0</span></span>
  <span>GBP/VUV =<span class="v">151.7</span></span>
</div>

<div class="abs verified">Verified and Protected by</div>
<div class="abs badge" style="left:219px;width:64px"></div>
<div class="abs badge" style="left:356px;width:62px;border-radius:3px"></div>
<div class="abs badge" style="left:490px;width:30px;height:30px;top:875px;border-radius:50%"></div>
<div class="abs badge" style="left:594px;width:54px;border-radius:2px"></div>

<!-- Footer -->
<div class="abs footer"></div>
<div class="abs footer-base"></div>

<div class="abs fcol" style="left:103px;width:85px">
  <h4>About Us</h4>
  <ul><li>History</li><li>Expertize</li><li>Idedtity</li><li>Strategy</li><li>Contact Us</li></ul>
</div>
<div class="abs fcol tight" style="left:208px;width:144px">
  <h4>Investments</h4>
  <ul><li>Term Deposits</li><li>Management &amp; Strategy</li><li>Client Relations</li><li>Financial Privacy</li><li>Tax Advice</li><li>Wealth Analysis &amp; Financial Planning</li><li>Active Advisory Group</li><li>Manager Selection Services</li><li>Private Equity</li></ul>
</div>
<div class="abs fcol" style="left:383px;width:95px">
  <h4>Funds</h4>
  <ul style="margin-top:6px"><li style="height:18px">Overview</li><li style="height:18px">Administration</li><li style="height:18px">Funds Security</li><li style="height:18px">Core Services</li><li style="height:18px">Reporting</li><li style="height:18px">Revenue Opportunities</li><li style="height:18px">How it works?</li><li style="height:18px">Glossary</li></ul>
</div>
<div class="abs fcol" style="left:506px;width:155px">
  <h4>Currancy Exchange</h4>
  <ul><li>Foreign Exchange</li><li>Fx Forword</li><li>Fx Options</li></ul>
</div>
<div class="abs fcol" style="left:506px;top:1035px;width:96px">
  <h4>Accounts</h4>
  <ul><li>Apply Now</li><li>Private Access</li></ul>
</div>
<div class="abs fcol" style="left:685px;width:86px">
  <h4>Brokerage</h4>
  <ul><li>Institutional</li><li>Research</li><li>Trading</li></ul>
</div>

<div class="abs legal">Lorem ipsum dolor sit amet, consectetuer elit, sed diam nonummy nibh euismod tincidunt ut laoreet dolore magna aliquam erat volutpat. Ut wisi enim ad minim veniam, quis nostrud exerci tation ullamcorper suscipit lobortis nisl ut aliquip ex ea commodo consequat. Duis autem vel eum iriure dolor in hendrerit in vulputate velit esse molestie consequat, vel illum dolore eu feugiat nulla facilisis at vero eros et accumsan et iusto odio dignissim qui blandit praesent luptatum zzril delenit augue duis dolore te feugait nulla facilisi.</div>
<div class="abs copy">© 2013 MarloweCapitalGroup &nbsp;| &nbsp;All Rights Reserved</div>

</body>
</html>
```